" Consultório odontológico diferenciado, sou formado há 28 anos, em fase de instalação, pequeno, mas com todos os equipamentos necessários para realizar odontologia de alto nível. "

```html
<!DOCTYPE html>
<html lang="pt-BR">
<head>
<meta charset="utf-8">
<title>LUMEN Odontologia — Pasta de documentos</title>
<link href="https://fonts.googleapis.com/css2?family=Cormorant+Garamond:wght@500&family=Montserrat:wght@400;500&display=swap" rel="stylesheet">
<style>
  :root {
    --navy: #141a4a;
    --navy-deep: #0b1036;
    --navy-light: #222a68;
    --gold-dark: #8a6a2a;
    --gold: #d8b868;
    --gold-light: #f4e2a8;
    --paper: #ffffff;
    --paper-shade: #e9eaee;
    --stage: #c9cacd;
    --stage-light: #ececee;
    --ink: #333;
    --silver: #b9bcc4;
  }
  * { margin: 0; padding: 0; box-sizing: border-box; }
  html, body { width: 1200px; height: 1200px; overflow: hidden; background: #fff; }
  .sheet {
    position: relative; width: 1200px; height: 1200px;
    background: radial-gradient(ellipse at 45% 45%, var(--stage-light) 0%, var(--stage) 80%);
    font-family: "Montserrat", sans-serif;
  }
  .sheet-label {
    position: absolute; left: 29px; top: 96px;
    font-size: 22px; color: #333; letter-spacing: 0.5px;
  }
  .folder { position: absolute; left: 149px; top: 163px; width: 936px; }
  .panel { position: absolute; top: 0; height: 581px; }
  .panel-inside {
    left: 0; width: 480px;
    background: linear-gradient(135deg, var(--paper-shade) 0%, var(--paper) 45%, var(--paper) 100%);
  }
  .panel-cover {
    left: 480px; width: 456px;
    background: radial-gradient(ellipse at 50% 45%, var(--navy-light) 0%, var(--navy) 55%, var(--navy-deep) 100%);
  }
  .gold-band {
    position: absolute; left: 0; top: 581px; width: 936px; height: 29px;
    background: linear-gradient(90deg, var(--gold-dark), var(--gold) 20%, var(--gold-light) 50%, var(--gold) 75%, var(--gold-dark));
  }
  .gold-band::after {
    content: ""; position: absolute; left: 0; right: 0; bottom: 0; height: 6px; background: var(--navy);
  }
  .pocket { position: absolute; left: 0; top: 610px; }
  .brand { position: absolute; display: flex; align-items: center; gap: 12px; }
  .brand-dot { border-radius: 50%; border: 2px solid var(--gold); flex: none; }
  .brand-text { display: flex; flex-direction: column; align-items: center; line-height: 1; }
  .brand-name { font-family: "Cormorant Garamond", serif; font-weight: 500; letter-spacing: 2px; }
  .brand-sub { font-family: "Montserrat", sans-serif; letter-spacing: 3px; margin-top: 4px; }
  .brand-inside { left: 140px; top: 470px; }
  .brand-inside .brand-dot { width: 34px; height: 34px; border-color: var(--navy); }
  .brand-inside .brand-name { font-size: 44px; color: var(--navy); }
  .brand-inside .brand-sub { font-size: 8px; color: var(--navy); }
  .brand-cover { left: 575px; top: 255px; }
  .brand-cover .brand-dot { width: 56px; height: 56px; }
  .brand-cover .brand-name { font-size: 66px; color: var(--silver); }
  .brand-cover .brand-sub { font-size: 11px; color: var(--gold); }
  .contact {
    position: absolute; left: 0; width: 480px; top: 538px;
    font-size: 11px; color: var(--ink); text-align: center; line-height: 20px;
  }
  .contact .sep { margin: 0 8px; }
  .web {
    position: absolute; left: 480px; width: 456px; top: 480px;
    text-align: center; font-size: 15px; letter-spacing: 3.5px; color: var(--silver);
  }
</style>
</head>
<body>
<main class="sheet">
  <p class="sheet-label">PASTA DE DOCUMENTOS</p>

  <section class="folder">
    <div class="panel panel-inside">
      <div class="brand brand-inside">
        <span class="brand-dot"></span>
        <span class="brand-text"><span class="brand-name">LUMEN</span><span class="brand-sub">ODONTOLOGIA</span></span>
      </div>
      <address class="contact" style="font-style:normal">
        +55 11 4000-0000<span class="sep">|</span>contato@lumenodonto.com.br<br>
        R. Acácias, 120 - Sala 4 - Centro - CEP 01000-000 / São Paulo-SP
      </address>
    </div>

    <div class="panel panel-cover">
      <div class="brand brand-cover" style="left:95px">
        <span class="brand-dot"></span>
        <span class="brand-text"><span class="brand-name">LUMEN</span><span class="brand-sub">ODONTOLOGIA</span></span>
      </div>
    </div>
    <p class="web">lumenodontologia.com.br</p>

    <div class="gold-band"></div>

    <svg class="pocket" width="480" height="380" viewBox="0 0 480 380">
      <defs>
        <linearGradient id="pocketFill" x1="0" y1="0" x2="1" y2="1">
          <stop offset="0" stop-color="#222a68"/>
          <stop offset="1" stop-color="#0b1036"/>
        </linearGradient>
      </defs>
      <path d="M0 0 H480 V150 C400 180 320 250 290 355 H40 C20 320 10 300 0 290 Z" fill="url(#pocketFill)"/>
      <line x1="200" y1="70" x2="226" y2="102" stroke="#fff" stroke-width="3"/>
      <line x1="45" y1="130" x2="72" y2="165" stroke="#fff" stroke-width="3"/>
    </svg>
  </section>
</main>
</body>
</html>
```